Business card and stationery
Harbor Lantern Kitchen
Professional
Dale Pritchard
1187 North Cedar Row
Bayview Harbor, CA. 90417
Daltonpritchard@quillmail.com
Leave room for: phone number, fax, email and web address

```html
<!DOCTYPE html>
<html lang="en">
<head>
<meta charset="utf-8">
<title>Harbor Lantern Kitchen — Business Cards</title>
<link href="https://fonts.googleapis.com/css2?family=Tinos:wght@400;700&display=swap" rel="stylesheet">
<style>
  :root {
    --bg: #e9e6e1;
    --card: #ffffff;
    --navy: #1f3f8f;
    --ink: #333333;
    --rule: #c9c9c9;
    --orange-light: #ffb43a;
    --orange-dark: #e86d0c;
    --shadow: rgba(0,0,0,0.18);
  }
  * { box-sizing: border-box; margin: 0; padding: 0; }
  html, body { width: 1200px; height: 852px; overflow: hidden; }
  body {
    background: var(--bg);
    font-family: "Tinos", "Times New Roman", serif;
    color: var(--ink);
    position: relative;
  }
  .card {
    position: absolute;
    width: 540px;
    height: 310px;
    background: var(--card);
    border-radius: 16px;
    overflow: hidden;
    box-shadow: 0 8px 22px var(--shadow);
  }
  .card--front { left: 70px; top: 80px; }
  .card--back { left: 590px; top: 462px; }

  .card__band {
    position: absolute;
    left: 0; right: 0; bottom: 0;
    height: 34px;
    border-top: 3px solid var(--navy);
    background: linear-gradient(to bottom, var(--orange-light), var(--orange-dark));
  }

  .brand {
    display: flex;
    align-items: center;
    gap: 12px;
    color: var(--navy);
    font-weight: 700;
    font-size: 22px;
    line-height: 1.15;
  }
  .brand__dot {
    flex: none;
    width: 26px; height: 26px;
    border-radius: 50%;
    background: var(--navy);
  }

  .card--front .brand {
    position: absolute;
    left: 30px; top: 110px;
    width: 230px;
  }
  .card--front .divider {
    position: absolute;
    left: 280px; top: 24px;
    width: 1px; height: 224px;
    background: var(--rule);
  }
  .card--front .details {
    position: absolute;
    left: 300px; top: 30px;
    width: 225px;
  }

  .person {
    color: var(--navy);
    font-weight: 700;
    font-size: 19px;
    margin-bottom: 22px;
  }
  .address {
    font-size: 13px;
    line-height: 1.35;
    margin-bottom: 24px;
  }
  .contacts { list-style: none; }
  .contacts li {
    display: flex;
    align-items: center;
    gap: 8px;
    font-size: 13px;
    line-height: 1.55;
    white-space: nowrap;
  }
  .icon { width: 12px; height: 12px; flex: none; fill: var(--navy); }

  .card--back .brand {
    position: absolute;
    left: 0; right: 0; top: 36px;
    justify-content: center;
    font-size: 24px;
  }
  .card--back .identity {
    position: absolute;
    left: 50px; top: 150px;
    width: 200px;
  }
  .card--back .person { margin-bottom: 12px; }
  .card--back .divider {
    position: absolute;
    left: 262px; top: 140px;
    width: 1px; height: 118px;
    background: var(--rule);
  }
  .card--back .contacts {
    position: absolute;
    left: 282px; top: 146px;
  }
</style>
</head>
<body>
  <svg width="0" height="0" style="position:absolute">
    <defs>
      <symbol id="icon-phone" viewBox="0 0 24 24"><path d="M6.6 10.8a15 15 0 0 0 6.6 6.6l2.2-2.2c.3-.3.7-.4 1-.2 1.1.4 2.3.6 3.6.6.6 0 1 .4 1 1V20c0 .6-.4 1-1 1A17 17 0 0 1 3 4c0-.6.4-1 1-1h3.5c.6 0 1 .4 1 1 0 1.3.2 2.5.6 3.6.1.3 0 .7-.2 1z"/></symbol>
      <symbol id="icon-mobile" viewBox="0 0 24 24"><path d="M7 1h10a2 2 0 0 1 2 2v18a2 2 0 0 1-2 2H7a2 2 0 0 1-2-2V3a2 2 0 0 1 2-2zm0 3v14h10V4zm5 15.2a1 1 0 1 0 0 2 1 1 0 0 0 0-2z"/></symbol>
      <symbol id="icon-mail" viewBox="0 0 24 24"><path d="M2 5h20v14H2zm2 2v.5l8 5 8-5V7zm0 3v7h16v-7l-8 5z"/></symbol>
      <symbol id="icon-web" viewBox="0 0 24 24"><path d="M12 2a10 10 0 1 0 0 20 10 10 0 0 0 0-20zm-1 2.1V8H7.3A8 8 0 0 1 11 4.1zm2 0A8 8 0 0 1 16.7 8H13zM5.3 10H11v4H5.3a8 8 0 0 1 0-4zM13 10h5.7a8 8 0 0 1 0 4H13zm-5.7 6H11v3.9A8 8 0 0 1 7.3 16zm5.7 0h3.7a8 8 0 0 1-3.7 3.9z"/></symbol>
    </defs>
  </svg>

  <article class="card card--front">
    <div class="brand">
      <span class="brand__dot"></span>
      <span class="brand__name">Harbor Lantern Kitchen</span>
    </div>
    <div class="divider"></div>
    <div class="details">
      <p class="person">Dale Pritchard</p>
      <p class="address">1187 North Cedar Row<br>Bayview Harbor, CA. 90417</p>
      <ul class="contacts">
        <li><svg class="icon"><use href="#icon-phone"/></svg>555 201 4470</li>
        <li><svg class="icon"><use href="#icon-mobile"/></svg>555 201 4471</li>
        <li><svg class="icon"><use href="#icon-mail"/></svg>Daltonpritchard@quillmail.com</li>
        <li><svg class="icon"><use href="#icon-web"/></svg>www.harborlantern.com</li>
      </ul>
    </div>
    <div class="card__band"></div>
  </article>

  <article class="card card--back">
    <div class="brand">
      <span class="brand__dot"></span>
      <span class="brand__name">Harbor Lantern Kitchen</span>
    </div>
    <div class="identity">
      <p class="person">Dale Pritchard</p>
      <p class="address">1187 North Cedar Row<br>Bayview Harbor, CA. 90417</p>
    </div>
    <div class="divider"></div>
    <ul class="contacts">
      <li><svg class="icon"><use href="#icon-phone"/></svg>555 201 4470</li>
      <li><svg class="icon"><use href="#icon-mobile"/></svg>555 201 4471</li>
      <li><svg class="icon"><use href="#icon-mail"/></svg>Daltonpritchard@quillmail.com</li>
      <li><svg class="icon"><use href="#icon-web"/></svg>www.harborlantern.com</li>
    </ul>
    <div class="card__band"></div>
  </article>
</body>
</html>
```